recipe card template

desgin an AI file that is a template for a recipe card. We are an Organic beef farm wanting to give customers recipe cards for our different beef cuts. Looking at doing something black & white that says premium product from a family farm.

Target Market(s)

people who want quality produce

Industry/Entity Type

Farm

Font styles to use
Serif
Sans Serif

Colors

Designer to choose colors to be used in the design.

Requirements
Must have
• Instruction section - ingredients section - "stonebrook larder family farm" title
Nice to have
• images etc that refer to beef and eggs

```html
<!DOCTYPE html>
<html lang="en">
<head>
<meta charset="utf-8">
<title>Stonebrook Larder Family Farm — Recipe Cards</title>
<link rel="stylesheet" href="https://fonts.googleapis.com/css2?family=Kaushan+Script&family=Oswald:wght@300;400&family=Lato:wght@400;700&display=swap">
<style>
  :root{
    --page:#e9e9e9;
    --card:#f4f4f4;
    --ink:#2b2b2b;
    --muted:#6d6d6d;
    --cow:#9a9a9a;
    --burger:#d48a10;
    --chuck:#6e9a5b;
    --flank:#7b3027;
    --black:#141414;
    --white:#ffffff;
  }
  *{box-sizing:border-box;margin:0;padding:0}
  html,body{width:1200px;height:686px;overflow:hidden;background:var(--page)}
  body{font-family:"Lato",sans-serif;color:var(--ink)}
  .sheet{
    width:1200px;height:686px;padding:13px 50px;
    display:grid;grid-template-columns:540px 540px;grid-template-rows:320px 320px;gap:20px;
    justify-content:center;
  }
  .card{display:flex;width:540px;height:320px;background:var(--card);box-shadow:0 2px 8px rgba(0,0,0,.18);overflow:hidden}
  .card--flank{grid-column:1 / span 2;justify-self:center}

  /* photo side */
  .photo-side{position:relative;width:200px;height:100%;flex:none;display:flex;flex-direction:column}
  .photo{flex:1}
  .farm-block{padding:14px 12px 12px;text-align:center}
  .farm-title{
    font-family:"Lato",sans-serif;font-weight:400;font-size:15px;line-height:1.2;text-transform:uppercase;letter-spacing:0;
    padding:6px 0 5px;margin-bottom:6px
  }
  .farm-meta{font-size:9.5px;line-height:1.45;text-transform:uppercase;letter-spacing:.3px}
  .farm-meta span{text-transform:none}

  .card--burger .farm-block{background:var(--black);color:var(--white);padding-top:22px}
  .card--burger .farm-title{color:var(--burger);border-top:1px solid var(--burger);border-bottom:1px solid var(--burger)}
  .card--burger .photo{background:linear-gradient(170deg,#3b2a1d 0%,#c78a3e 25%,#e2b04a 40%,#5a8a2a 52%,#b4321c 60%,#4a2614 74%,#2a1a10 100%)}

  .card--chuck .photo{background:radial-gradient(ellipse at 55% 55%,#7a4a30 0%,#4e2c1c 45%,#1f1a17 80%)}
  .card--chuck .farm-block{position:absolute;left:0;right:0;bottom:0;background:linear-gradient(to top,rgba(15,15,15,.9),rgba(15,15,15,.55));color:var(--white)}
  .card--chuck .farm-title{color:#b8d7a2;border-top:1px solid var(--chuck);border-bottom:1px solid var(--chuck)}

  .card--flank .photo{background:linear-gradient(to bottom,#ffffff 0%,#f3efe9 30%,#8c5a3a 50%,#5b2e1e 70%,#b45e55 85%,#3a1e14 100%)}
  .card--flank .farm-block{position:absolute;left:0;right:0;top:0;color:var(--flank);background:linear-gradient(to bottom,#fff 70%,rgba(255,255,255,0))}
  .card--flank .farm-title{border-top:1px solid var(--flank);border-bottom:1px solid var(--flank)}
  .card--flank .farm-meta{color:var(--ink)}

  /* recipe side */
  .recipe-side{flex:1;display:flex;flex-direction:column;min-width:0}
  .recipe-name{
    flex:none;height:50px;padding:4px 16px;color:var(--white);
    font-family:"Kaushan Script",cursive;font-weight:400;font-size:30px;line-height:42px;white-space:nowrap
  }
  .card--burger .recipe-name{background:var(--burger)}
  .card--chuck .recipe-name{background:var(--chuck)}
  .card--flank .recipe-name{background:var(--flank)}
  .recipe-body{flex:none;padding:10px 18px 0}
  .section-head{font-family:"Oswald",sans-serif;font-weight:300;font-size:17px;text-transform:uppercase;line-height:1.1}
  .card--burger .section-head{color:var(--burger)}
  .card--chuck .section-head{color:var(--chuck)}
  .card--flank .section-head{color:var(--flank)}
  .section-text{font-size:11px;color:var(--muted);margin:2px 0 22px}
  .ingredient-cols{display:flex;gap:14px;font-size:8px;line-height:1.3;color:var(--ink);margin:2px 0 6px}
  .ingredient-cols ul{list-style:none}
  .method{font-size:8px;line-height:1.3;color:var(--ink);margin-top:2px}

  .recipe-foot{margin-top:auto;padding:0 14px 12px;display:flex;align-items:flex-end;justify-content:space-between}
  .cut-chart{display:block;flex:none}
  .follow{font-size:9px;color:var(--muted);text-align:right;line-height:1.5}
  .follow-handle{font-size:9px;color:var(--muted)}
</style>
</head>
<body>
<main class="sheet">

  <!-- Beef Burger -->
  <article class="card card--burger">
    <div class="photo-side">
      <div class="farm-block">
        <h2 class="farm-title">Stonebrook Larder<br>Family Farm</h2>
        <p class="farm-meta">Total time: <span>45 minutes</span><br>Servings: 2</p>
      </div>
      <div class="photo" role="img" aria-label="Photo of a beef burger with cheese, lettuce and tomato"></div>
    </div>
    <div class="recipe-side">
      <h1 class="recipe-name">Beef Burger</h1>
      <div class="recipe-body">
        <h3 class="section-head">Ingredients:</h3>
        <div class="ingredient-cols">
          <ul>
            <li>500G Stonebrook Larder Beef mince</li>
            <li>2 cloves garlic, crushed</li>
            <li>2 tbsp Worcestershire sauce</li>
            <li>fresh thyme, rosemary, oregano</li>
            <li>chopped finely</li>
            <li>5 Stonebrook Larder Eggs</li>
          </ul>
          <ul>
            <li>4 Bread rolls</li>
            <li>4 shortcut bacon</li>
            <li>1 red onion</li>
            <li>4 slices cheese</li>
            <li>8 slices tomato</li>
            <li>4 slices beetroot</li>
          </ul>
        </div>
        <h3 class="section-head">Instruction:</h3>
        <p class="method">In a bowl, mix mince, garlic, Worcestershire sauce and herbs with your hands until all well combined. Divide into quarters and shape patties. Heat a pan, add oil, and cook burgers both sides. Once browned, add bacon and onion, cook both sides until caramalised. In another pan, cook the cheese. Remove bacon and onion from pan. Fry eggs in the pan. Build rolls with the salad ingredients, then top with the cooked ingredients.</p>
      </div>
      <div class="recipe-foot">
        <svg class="cut-chart" width="118" height="72" viewBox="0 0 150 92" role="img" aria-label="Beef cut chart with the mince cut highlighted">
          <rect x="0" y="0" width="150" height="92" rx="8" fill="var(--cow)"/>
          <rect x="58" y="6" width="16" height="30" fill="var(--burger)"/>
        </svg>
        <div class="follow">find us on:<br><span class="follow-handle">@stonebrooklarder</span></div>
      </div>
    </div>
  </article>

  <!-- Chuck Recipe -->
  <article class="card card--chuck">
    <div class="photo-side">
      <div class="photo" role="img" aria-label="Photo of a grilled chuck steak with herbs, tomatoes and zucchini"></div>
      <div class="farm-block">
        <h2 class="farm-title">Stonebrook Larder<br>Family Farm</h2>
        <p class="farm-meta">Total time: <span>45 minutes</span><br>Servings: 2</p>
      </div>
    </div>
    <div class="recipe-side">
      <h1 class="recipe-name">Chuck Recipe</h1>
      <div class="recipe-body">
        <h3 class="section-head">Ingredients:</h3>
        <p class="section-text">Lorem ipsum</p>
        <h3 class="section-head">Instruction:</h3>
        <p class="section-text">Lorem ipsum</p>
      </div>
      <div class="recipe-foot">
        <svg class="cut-chart" width="170" height="104" viewBox="0 0 170 104" role="img" aria-label="Beef cut chart with the chuck cut highlighted">
          <rect x="0" y="0" width="170" height="104" rx="8" fill="var(--cow)"/>
          <rect x="100" y="6" width="24" height="44" fill="var(--chuck)"/>
        </svg>
        <div class="follow">find us on:<br><span class="follow-handle">@stonebrooklarder</span></div>
      </div>
    </div>
  </article>

  <!-- Flank Steak -->
  <article class="card card--flank">
    <div class="photo-side">
      <div class="photo" role="img" aria-label="Photo of sliced seared flank steak with herbs and rosemary"></div>
      <div class="farm-block">
        <h2 class="farm-title">Stonebrook Larder<br>Family Farm</h2>
        <p class="farm-meta">Total time: <span>45 minutes</span><br>Servings: 2</p>
      </div>
    </div>
    <div class="recipe-side">
      <h1 class="recipe-name">Flank Steak</h1>
      <div class="recipe-body">
        <h3 class="section-head">Ingredients:</h3>
        <p class="section-text">Lorem ipasum</p>
        <h3 class="section-head">Instruction:</h3>
        <p class="section-text">Lorem ipasum</p>
      </div>
      <div class="recipe-foot">
        <svg class="cut-chart" width="170" height="104" viewBox="0 0 170 104" role="img" aria-label="Beef cut chart with the flank cut highlighted">
          <rect x="0" y="0" width="170" height="104" rx="8" fill="var(--cow)"/>
          <rect x="60" y="56" width="30" height="20" fill="var(--flank)"/>
        </svg>
        <div class="follow">find us on:<br><span class="follow-handle">@stonebrooklarder</span></div>
      </div>
    </div>
  </article>

</main>
</body>
</html>
```